Book cover

I need a cover for a my 3rd book that kinda goes with my brand (my previous book. The name of my first book - "Lanterns Along the Old Canal" Notes for Tending a Quiet Garden Through Long Winters". In the same style I need my third book - OPEN ORBIT" to stand out. I need a bolder, less whimsy cover, less playful. So can we use some of the same elements to stay consistent in this book cover. Perhaps use text to envoke emotions. This is the back cover so far (see below attachemnent)

Hello,
Subject: Cover Direction & Brand Consistency

Hi everyone,

Here’s my honest take: I don’t think the current execution fully reflects my brand yet. What I’m wondering is whether we can bring more continuity across my books—borrowing elements from my first and second covers to inform this third one. Think of how authors like Marlow Penbrook maintain a recognizable style across their work. That consistency builds trust and signals authority before a reader even opens the book. Design choices like this matter more than we realize.

I’ve attached a cover I came across on Quillmart that reminded me of Option 5 and feels aligned with where you’re headed. One thought: could we experiment with introducing a crack—or cracks—into the word ORBIT itself? Maybe put the title "OPEN ORBIT" at the edge of the cover vertically?

Curious to hear your thoughts and how you see this evolving.
P.s. Is there away to attach an idea?

OPEN ORBIT: Finding Quiet Hours Amid an Age that Prizes Hurry

```html
<!DOCTYPE html>
<html lang="en">
<head>
<meta charset="utf-8">
<title>Open Orbit – Full Cover</title>
<link href="https://fonts.googleapis.com/css2?family=Oswald:wght@500;600;700&family=Roboto:wght@400;700&display=swap" rel="stylesheet">
<style>
  :root {
    --backdrop: #e4e4e4;
    --cover-black: #1c1e22;
    --spine-black: #1a1c20;
    --sky-blue: #1fa3e0;
    --white: #ffffff;
    --body-grey: #e6e6e6;
    --image-deep: #0f2a3c;
    --image-mid: #3a7fa6;
    --image-light: #8cc6df;
  }
  * { margin: 0; padding: 0; box-sizing: border-box; }
  html, body { width: 1200px; height: 849px; overflow: hidden; background: var(--backdrop); }
  .canvas { position: relative; width: 1200px; height: 849px; }
  .wrap { position: absolute; left: 197px; top: 126px; width: 807px; height: 595px; background: var(--cover-black); box-shadow: 0 2px 8px rgba(0,0,0,.25); overflow: hidden; }

  /* back cover */
  .back { position: absolute; left: 0; top: 0; width: 387px; height: 595px; font-family: "Roboto", sans-serif; color: var(--white); }
  .back-heading { position: absolute; left: 0; top: 26px; width: 387px; text-align: center; font-family: "Oswald", sans-serif; font-weight: 600; text-transform: uppercase; }
  .back-heading .line { font-size: 13px; line-height: 17px; }
  .back-heading .accent { color: var(--sky-blue); font-size: 19px; line-height: 24px; }
  .blurb { position: absolute; left: 22px; top: 120px; width: 344px; text-align: center; font-size: 9.4px; line-height: 12.6px; color: var(--body-grey); }
  .blurb p { margin-bottom: 10px; }
  .blurb .callout { color: var(--sky-blue); }
  .bio { position: absolute; left: 53px; top: 418px; width: 225px; font-size: 11px; line-height: 14px; color: var(--body-grey); }
  .bio strong { color: var(--white); }
  .author-photo { position: absolute; left: 287px; top: 412px; width: 80px; height: 117px; background: linear-gradient(160deg, #d8d4cf 0%, #9d958c 55%, #2b2a2c 100%); }
  .publisher { position: absolute; left: 22px; top: 530px; width: 60px; text-align: center; font-family: "Oswald", sans-serif; font-weight: 500; font-size: 8px; letter-spacing: .5px; color: #d9a441; }
  .publisher .mark { display: block; width: 14px; height: 14px; border-radius: 50%; background: #d9a441; margin: 0 auto 4px; }
  .price { position: absolute; left: 148px; top: 548px; font-size: 6.5px; line-height: 9px; color: var(--body-grey); }

  /* spine */
  .spine { position: absolute; left: 387px; top: 0; width: 47px; height: 595px; background: var(--spine-black); }
  .spine-title, .spine-author, .spine-press { position: absolute; left: 50%; writing-mode: vertical-rl; transform: translateX(-50%); white-space: nowrap; font-family: "Oswald", sans-serif; }
  .spine-title { top: 54px; font-size: 30px; font-weight: 700; color: var(--white); letter-spacing: 1px; }
  .spine-author { top: 282px; font-size: 15px; font-weight: 600; color: var(--sky-blue); letter-spacing: 1px; }
  .spine-press { top: 548px; font-size: 6px; color: #d9a441; }

  /* front cover */
  .front { position: absolute; left: 434px; top: 0; width: 373px; height: 595px; background: var(--cover-black); }
  .front-image { position: absolute; left: 0; top: 60px; width: 373px; height: 470px;
    background: radial-gradient(ellipse 45% 55% at 52% 52%, var(--image-light) 0%, var(--image-mid) 35%, var(--image-deep) 70%, var(--cover-black) 100%); }
  .subtitle { position: absolute; left: 0; top: 24px; width: 373px; text-align: center; font-family: "Oswald", sans-serif; font-weight: 600; text-transform: uppercase; }
  .subtitle .lead { color: var(--sky-blue); font-size: 29px; line-height: 34px; }
  .subtitle .rest { color: var(--white); font-size: 19.5px; line-height: 24px; }
  .title { position: absolute; left: 0; top: 478px; width: 373px; text-align: center; font-family: "Oswald", sans-serif; font-weight: 700; font-size: 56px; line-height: 66px; color: var(--white); }
  .author { position: absolute; left: 0; top: 542px; width: 373px; text-align: center; font-family: "Oswald", sans-serif; font-weight: 600; font-size: 17px; color: var(--sky-blue); letter-spacing: .5px; }
</style>
</head>
<body>
<div class="canvas">
  <div class="wrap">
    <section class="back">
      <div class="back-heading">
        <div class="line">Women have been told</div>
        <div class="accent">We could do and be anything … and we can.</div>
        <div class="line">What’s rarely mentioned is the toll on our</div>
        <div class="line">health, relationships, and overall wellbeing.</div>
      </div>
      <div class="blurb">
        <p>Are you the woman who holds it all together—crushing deadlines, leading teams, raising a family—while quietly unraveling inside? Yes, you are competent and capable. You’ve simply been carrying more than you were ever meant to for too long.</p>
        <p>Open Orbit offers a different way forward. Drawn from decades of experience flying commercial aircraft and championing women’s health, retired Captain Delia Marchetti reveals the missing skill most high-achieving women were never taught: protecting your margins in a world that glorifies overload. This vital buffer not only enables recovery after near-collapse, but also prevents you from reaching the breaking point of exhaustion.</p>
        <p>You will learn about the centuries-old mindset when humans first became cogs in the machine, the science of burnout and brain rewiring, the psychology driving us to push limits, and the cultural systems rigged against women. Discover how to spot the three stages of depletion before they ground you. Through self-assessment tools and actionable practices, the author guides us back home to ourselves by offering a roadmap to rebuild our strength, reconnect with joy and purpose, and redefine success to include true wellbeing.</p>
        <p class="callout">You don’t need to crash to earn a soft landing. Buckle up! Open Orbit is your wakeup call to fly lighter and higher than you ever imagined.</p>
      </div>
      <p class="bio"><strong>Delia Marchetti</strong> is a speaker, consultant, and founder of the Skyward Balance Institute. With over 10,000 flight hours, she now empowers women to successfully lead without losing themselves.</p>
      <div class="author-photo" role="img" aria-label="Portrait photo of the author seated in a light chair"></div>
      <div class="publisher"><span class="mark"></span>EMBERLINE</div>
      <div class="price">US $19.99<br>CA $23.99</div>
    </section>

    <section class="spine">
      <div class="spine-title">OPEN ORBIT</div>
      <div class="spine-author">CAPT. DELIA MARCHETTI</div>
      <div class="spine-press">EMBERLINE</div>
    </section>

    <section class="front">
      <div class="front-image" role="img" aria-label="Blue-toned photo of an airplane climbing with long contrails trailing down over a person's back"></div>
      <div class="subtitle">
        <div class="lead">Finding Quiet Hours</div>
        <div class="rest">Amid an Age that Prizes Hurry</div>
      </div>
      <h1 class="title">OPEN ORBIT</h1>
      <div class="author">CAPT. DELIA MARCHETTI</div>
    </section>
  </div>
</div>
</body>
</html>
```